Company director needs a business card design

I am a semi-retired former senior finance executive who sits on a number of public and private company boards and do some consulting work. I work largely with emerging businesses but deal regularly with top end of town lawyers, bankers etc. I need a thoughtful but relatively conservative design which would also resonate with my younger client base. Some colour would be good. Information limited to name, address, office tel, mobile and email.

Industry/Entity Type

Finance

```html
<!DOCTYPE html>
<html lang="en">
<head>
<meta charset="utf-8">
<title>Business Card – Company Director</title>
<link href="https://fonts.googleapis.com/css2?family=Tinos:wght@400&display=swap" rel="stylesheet">
<style>
  :root {
    --card-black: #000000;
    --accent-red: #ee0000;
    --text-white: #ffffff;
    --text-black: #0a0a0a;
    --backdrop: #e9e6e1;
  }
  * { margin: 0; padding: 0; box-sizing: border-box; }
  html, body {
    width: 1200px;
    height: 800px;
    overflow: hidden;
    background: var(--backdrop);
  }
  .business-card {
    position: absolute;
    left: 100px;
    top: 114px;
    width: 1000px;
    height: 572px;
    overflow: hidden;
    font-family: "Tinos", "Times New Roman", serif;
  }
  .card-shapes {
    position: absolute;
    inset: 0;
    width: 1000px;
    height: 572px;
  }
  .card-name {
    position: absolute;
    left: 500px;
    width: 300px;
    top: 52px;
    text-align: center;
    color: var(--text-white);
    font-size: 40px;
    letter-spacing: 1px;
    white-space: nowrap;
  }
  .contact-list {
    position: absolute;
    left: 370px;
    top: 196px;
    list-style: none;
  }
  .contact-item {
    display: flex;
    align-items: center;
    height: 46px;
    color: var(--text-white);
    font-size: 26px;
    letter-spacing: 0.5px;
    white-space: nowrap;
  }
  .contact-icon {
    width: 24px;
    height: 24px;
    margin-right: 34px;
    fill: var(--text-white);
  }
  .card-address {
    position: absolute;
    left: 90px;
    top: 490px;
    color: var(--text-black);
    font-size: 29px;
    letter-spacing: 0.5px;
    white-space: nowrap;
  }
</style>
</head>
<body>
  <div class="business-card">
    <svg class="card-shapes" viewBox="0 0 1000 572" aria-hidden="true">
      <rect class="card-base" width="1000" height="572" fill="var(--card-black)"/>
      <polygon class="name-tab" points="520,0 790,0 790,10 762,34 548,34 520,10" fill="var(--accent-red)"/>
      <polygon class="address-band" points="0,392 1000,392 1000,572 0,572" fill="var(--accent-red)"/>
      <polygon class="contact-tab" points="320,392 640,392 640,460 616,482 344,482 320,460" fill="var(--card-black)"/>
    </svg>

    <div class="card-name">Your Name</div>

    <ul class="contact-list">
      <li class="contact-item">
        <svg class="contact-icon" viewBox="0 0 24 24"><path d="M6.6 2.5c.6-.3 1.3-.1 1.6.5l1.7 3.2c.3.6.1 1.3-.4 1.7L8 8.9c.9 2.4 2.8 4.9 5 6.3l1.2-1.3c.5-.5 1.2-.6 1.8-.2l3 2c.6.4.7 1.1.4 1.7l-1.4 2.2c-.6.9-1.7 1.3-2.7.9C9.4 18.3 4.8 12.5 4 6.3c-.1-1 .4-2 1.3-2.6z"/></svg>
        <span>+1 (555) 0142 736</span>
      </li>
      <li class="contact-item">
        <svg class="contact-icon" viewBox="0 0 24 24"><path d="M7 1h10a2 2 0 0 1 2 2v18a2 2 0 0 1-2 2H7a2 2 0 0 1-2-2V3a2 2 0 0 1 2-2zm0 3v14h10V4zm5 15.2a1.1 1.1 0 1 0 0 2.2 1.1 1.1 0 0 0 0-2.2z"/></svg>
        <span>+1 (555) 0198 254</span>
      </li>
      <li class="contact-item">
        <svg class="contact-icon" viewBox="0 0 24 24"><path d="M2 5h20v14H2zm2 2v.4l8 5.6 8-5.6V7zm0 2.8V17h16V9.8l-8 5.6z"/></svg>
        <span>mail@kelvane.com</span>
      </li>
    </ul>

    <div class="card-address">48 Arden St.,&nbsp; Kelmont, NY 10482 P.O. Box: 207519</div>
  </div>
</body>
</html>
```